Cover for a recovery from breast augmentation surgery pamphlet

Need a cover which includes my logo for new pamphlet on recovering from breast augmentation surgery It is just a quick how to guide.
I would like the cover to incorporate the Borela logo(2 options given) and be simple and clean. Will require in a vector file as well.

The title:
Well, Your Chest Is Upgraded...
WHAT NEXT?!

By: Borela

A little about me: I am an adult industry writer and am looking to do a mainstream project. This is a project I want to appeal to mainstream women.

Target Market(s)

Women who are recovering from or entertaining breast augmentation surgery

Font styles to use
Serif

Requirements
Must have
• One Borela logo, titile, and by Borela
Nice to have
• i love modern clean sleek design that is easy to read
Should not have
• nothing that would offend women or make them uncomfortable about their body

```html
<!DOCTYPE html>
<html lang="en">
<head>
<meta charset="utf-8">
<title>Borela – Recovery Guide Cover</title>
<link rel="stylesheet" href="https://fonts.googleapis.com/css2?family=Lato:wght@400&display=swap">
<style>
  :root {
    --paper: #f2f2f2;
    --pink-light: #e4519d;
    --pink-mid: #d13c93;
    --pink-deep: #bb2288;
    --pill: #ea4c9d;
    --water-light: #d6e8f1;
    --water-mid: #b3d4e4;
    --water-deep: #9cc5da;
    --white: #ffffff;
  }
  html, body {
    margin: 0;
    padding: 0;
    width: 907px;
    height: 1200px;
    overflow: hidden;
    background: var(--paper);
  }
  .cover {
    position: relative;
    width: 907px;
    height: 1200px;
    background: var(--paper);
    font-family: "Lato", "Gill Sans", sans-serif;
    overflow: hidden;
  }
  .cover-shapes {
    position: absolute;
    inset: 0;
  }
  .brand {
    position: absolute;
    top: 196px;
    left: 0;
    width: 907px;
    display: flex;
    justify-content: center;
    align-items: center;
    gap: 16px;
  }
  .brand-dot {
    width: 22px;
    height: 22px;
    border-radius: 50%;
    background: var(--pink-mid);
  }
  .brand-name {
    font-size: 76px;
    font-weight: 400;
    color: var(--pink-mid);
    letter-spacing: 1px;
    line-height: 1;
  }
  .title {
    position: absolute;
    top: 548px;
    left: 0;
    width: 907px;
    margin: 0;
    text-align: center;
    color: var(--white);
    font-weight: 400;
    font-size: 47px;
    line-height: 76px;
  }
  .title span { display: block; }
  .byline {
    position: absolute;
    left: 296px;
    top: 1102px;
    width: 299px;
    height: 57px;
    border-radius: 14px;
    background: var(--pill);
    color: var(--white);
    font-size: 30px;
    line-height: 57px;
    text-align: center;
  }
</style>
</head>
<body>
<main class="cover">
  <svg class="cover-shapes" width="907" height="1200" viewBox="0 0 907 1200" xmlns="http://www.w3.org/2000/svg">
    <defs>
      <linearGradient id="band-gradient" x1="0" y1="0" x2="1" y2="0">
        <stop offset="0" stop-color="var(--pink-light)"/>
        <stop offset="1" stop-color="var(--pink-deep)"/>
      </linearGradient>
      <linearGradient id="edge-gradient" x1="0" y1="0" x2="1" y2="0">
        <stop offset="0" stop-color="#b91f85"/>
        <stop offset="0.6" stop-color="#d2398f"/>
        <stop offset="1" stop-color="#ee5da3"/>
      </linearGradient>
      <linearGradient id="water-gradient" x1="0" y1="0" x2="0" y2="1">
        <stop offset="0" stop-color="var(--water-mid)"/>
        <stop offset="0.45" stop-color="var(--water-light)"/>
        <stop offset="1" stop-color="var(--water-deep)"/>
      </linearGradient>
    </defs>
    <!-- main pink band -->
    <path class="title-band" d="M0,329 Q380,520 907,387 L907,900 L0,900 Z" fill="url(#band-gradient)"/>
    <!-- darker sweep under the white header -->
    <path class="band-edge" d="M0,329 Q380,520 907,387 L907,405 Q400,520 0,370 Z" fill="url(#edge-gradient)"/>
    <!-- lighter lobe on the right -->
    <path class="band-lobe" d="M520,760 Q760,700 907,610 L907,870 Z" fill="#e4509c" opacity="0.55"/>
    <!-- photo area -->
    <path class="cover-photo" role="img" aria-label="Photo: a woman resting in calm, pale blue water with her reflection below"
          d="M0,790 Q300,815 627,738 Q820,760 907,862 L907,1200 L0,1200 Z" fill="url(#water-gradient)"/>
  </svg>

  <div class="brand">
    <span class="brand-dot"></span>
    <span class="brand-name">Borela</span>
  </div>

  <h1 class="title">
    <span>Well, Your Chest Is Upgraded...</span>
    <span>WHAT NEXT?!</span>
  </h1>

  <div class="byline">By: Borela</div>
</main>
</body>
</html>
```